Instagram post design for clothing brand

please see the attached design brief PDF

I will raise the budget for designs so I want to provide more submissions and designs
I have extended the deadline for submissions by one week extra

Requirements
Must have
• I want t-shirt mockup so I can put any design I want

```html
<!DOCTYPE html>
<html lang="en">
<head>
<meta charset="utf-8">
<title>Veltra Clothing – Launch Posts and Stories</title>
<link rel="stylesheet" href="https://fonts.googleapis.com/css2?family=Anton&family=Bebas+Neue&family=Montserrat:wght@600;700&display=swap">
<style>
  :root {
    --blue: #1a96d4;
    --black: #0d0d0d;
    --white: #ffffff;
    --grey: #d6d6d6;
    --ring-grey: #6e6e6e;
    --page: #d2d2d2;
    --tee-top: #ffffff;
    --tee-bottom: #e4e4e4;
  }
  * { box-sizing: border-box; margin: 0; padding: 0; }
  html, body { width: 906px; height: 1200px; overflow: hidden; }
  body { background: var(--page); position: relative; font-family: "Montserrat", sans-serif; }

  .post-row { position: absolute; top: 200px; left: 17px; display: flex; gap: 8px; }
  .post { position: relative; width: 212px; height: 212px; overflow: hidden; }
  .story-row { position: absolute; top: 480px; left: 13px; display: flex; gap: 20px; }
  .story { position: relative; width: 280px; height: 498px; overflow: hidden; }

  .layer { position: absolute; }
  .photo { position: absolute; }

  /* T-shirt mockup area: flat soft fill with the brand print placed on it */
  .tee {
    position: absolute;
    background: linear-gradient(180deg, var(--tee-top) 0%, var(--tee-bottom) 100%);
    border-radius: 10px;
    box-shadow: 0 2px 5px rgba(0,0,0,.14);
    display: flex; flex-direction: column; align-items: center; justify-content: center;
  }
  .tee-print { display: flex; flex-direction: column; align-items: center; gap: 2px; }
  .tee-print .brand-square { background: var(--black); }
  .tee-print .brand-name { font-family: "Bebas Neue", sans-serif; color: var(--blue); line-height: 1; letter-spacing: .5px; }

  .brand { position: absolute; display: flex; flex-direction: column; align-items: center; gap: 3px; }
  .brand-square { background: var(--black); }
  .brand-name { font-family: "Bebas Neue", sans-serif; color: var(--blue); letter-spacing: 1px; line-height: 1; }

  .headline { position: absolute; font-family: "Anton", sans-serif; line-height: 1.02; letter-spacing: .5px; white-space: nowrap; }
  .headline .line-blue { color: var(--blue); display: block; }
  .headline .line-black { color: var(--black); display: block; }

  .ring { position: absolute; }
  .ring-label { position: absolute; inset: 0; display: flex; flex-direction: column; align-items: center; justify-content: center; font-family: "Bebas Neue", sans-serif; color: var(--white); line-height: 1.05; text-align: center; }

  .contacts { position: absolute; font-size: 5px; font-weight: 700; color: var(--black); line-height: 1.7; white-space: nowrap; }
  .contacts .dot { display: inline-block; width: 4px; height: 4px; border-radius: 50%; background: var(--blue); margin-right: 3px; vertical-align: middle; }
  .contact-bar { position: absolute; left: 0; right: 0; bottom: 0; background: var(--black); color: var(--white); display: flex; justify-content: space-around; align-items: center; font-weight: 700; white-space: nowrap; }
  .contact-bar .dot { display: inline-block; width: 5px; height: 5px; border-radius: 50%; background: var(--blue); margin-right: 4px; vertical-align: middle; }
  .handle { position: absolute; display: flex; align-items: center; gap: 4px; font-weight: 600; white-space: nowrap; }
  .handle .dot { width: 8px; height: 8px; border-radius: 50%; background: var(--blue); }
</style>
</head>
<body>

<section class="post-row">

  <!-- Post 1: brand reveal -->
  <article class="post post-brand" style="background: var(--black);">
    <svg class="layer" width="212" height="212" viewBox="0 0 212 212" aria-hidden="true">
      <polygon fill="var(--blue)" points="4,6 60,2 110,9 170,3 188,12 184,60 192,110 180,160 190,205 120,210 60,206 30,200 22,160 28,110 18,70 12,30"/>
    </svg>
    <div class="brand" style="left:0; right:0; top:58px;">
      <span class="brand-square" style="width:64px; height:64px;"></span>
      <span class="brand-name" style="font-size:34px; color: var(--white);">VELTRA</span>
    </div>
  </article>

  <!-- Post 2: soon 35% -->
  <article class="post post-soon" style="background: var(--white);">
    <div class="photo" role="img" aria-label="Photo of a woman in a white tee and jeans beside a clothes rail" style="left:112px; top:0; width:100px; height:212px; background: linear-gradient(160deg,#5a4a40,#2f2622 60%,#8c8f99);"></div>
    <svg class="layer" width="212" height="212" viewBox="0 0 212 212" aria-hidden="true">
      <polygon fill="var(--black)" points="112,0 124,0 118,40 128,70 114,110 126,150 116,212 104,212 110,160 100,120 112,80 104,40"/>
      <rect x="9" y="10" width="194" height="192" fill="none" stroke="var(--blue)" stroke-width="1"/>
    </svg>
    <div class="brand" style="left:18px; width:76px; top:18px;">
      <span class="brand-square" style="width:32px; height:36px;"></span>
      <span class="brand-name" style="font-size:17px;">VELTRA</span>
    </div>
    <div class="headline" style="left:16px; top:80px; font-size:21px;">
      <span class="line-blue">VELTRA</span><span class="line-black">CLOTHING</span>
    </div>
    <div class="tee" role="img" aria-label="White t-shirt mockup with brand print" style="left:16px; top:136px; width:36px; height:38px;">
      <div class="tee-print"><span class="brand-square" style="width:8px; height:8px;"></span><span class="brand-name" style="font-size:5px;">VELTRA</span></div>
    </div>
    <div class="tee" role="img" aria-label="White t-shirt mockup with brand print" style="left:56px; top:136px; width:36px; height:38px;">
      <div class="tee-print"><span class="brand-square" style="width:8px; height:8px;"></span><span class="brand-name" style="font-size:5px;">VELTRA</span></div>
    </div>
    <div class="contacts" style="left:16px; top:180px;">
      <div><span class="dot"></span>0100.222.3344</div>
      <div><span class="dot"></span>www.veltra.shop</div>
      <div><span class="dot"></span>www.veltra.style</div>
    </div>
    <div class="ring" style="left:86px; top:132px; width:60px; height:60px;">
      <svg width="60" height="60" viewBox="0 0 60 60" aria-hidden="true">
        <circle cx="30" cy="30" r="26" fill="var(--ring-grey)"/>
        <circle cx="30" cy="30" r="28" fill="none" stroke="var(--white)" stroke-width="3" stroke-dasharray="62 114" transform="rotate(90 30 30)"/>
      </svg>
      <div class="ring-label"><span style="font-size:10px;">SOON</span><span style="font-size:12px;">35%</span></div>
    </div>
  </article>

  <!-- Post 3: very very soon 99% -->
  <article class="post post-very-very-soon" style="background: var(--grey);">
    <svg class="layer" width="212" height="212" viewBox="0 0 212 212" aria-hidden="true">
      <polygon fill="var(--black)" points="0,0 212,0 212,2 150,8 100,4 60,12 30,8 0,18"/>
    </svg>
    <div class="photo" role="img" aria-label="Photo of a smiling young man wearing a white tee" style="left:130px; top:60px; width:82px; height:152px; background: linear-gradient(170deg,#8a6a55 0%,#d9c2b0 30%,#f4f4f4 55%,#e6e6e6);"></div>
    <svg class="layer" width="212" height="212" viewBox="0 0 212 212" aria-hidden="true">
      <polygon fill="var(--white)" points="150,6 206,6 206,58 178,70 150,58"/>
    </svg>
    <div class="brand" style="left:150px; width:56px; top:12px;">
      <span class="brand-square" style="width:24px; height:24px;"></span>
      <span class="brand-name" style="font-size:12px;">VELTRA</span>
    </div>
    <div class="headline" style="left:12px; top:34px; font-size:27px;">
      <span class="line-black">VELTRA</span><span class="line-blue">CLOTHING</span>
    </div>
    <div class="tee" role="img" aria-label="White t-shirt mockup with brand print" style="left:12px; top:112px; width:40px; height:56px;">
      <div class="tee-print"><span class="brand-square" style="width:9px; height:9px;"></span><span class="brand-name" style="font-size:5px;">VELTRA</span></div>
    </div>
    <div class="tee" role="img" aria-label="White t-shirt mockup with brand print" style="left:56px; top:104px; width:44px; height:62px;">
      <div class="tee-print"><span class="brand-square" style="width:10px; height:10px;"></span><span class="brand-name" style="font-size:5px;">VELTRA</span></div>
    </div>
    <div class="ring" style="left:80px; top:112px; width:66px; height:66px;">
      <svg width="66" height="66" viewBox="0 0 66 66" aria-hidden="true">
        <circle cx="33" cy="33" r="29" fill="var(--ring-grey)"/>
        <circle cx="33" cy="33" r="31" fill="none" stroke="var(--white)" stroke-width="3" stroke-dasharray="190 5" transform="rotate(-90 33 33)"/>
      </svg>
      <div class="ring-label"><span style="font-size:9px;">VERY VERY</span><span style="font-size:9px;">SOON</span><span style="font-size:11px;">99%</span></div>
    </div>
    <div class="handle" style="left:12px; top:186px; font-size:6px; color:#333;"><span class="dot"></span>@veltraclothing.com</div>
  </article>

  <!-- Post 4: very soon 75% -->
  <article class="post post-very-soon" style="background: var(--white);">
    <div class="photo" role="img" aria-label="Photo of a woman and a man in white tees outdoors among greenery" style="left:0; top:0; width:130px; height:186px; background: linear-gradient(180deg,#4d5e3a 0%,#7d8a62 40%,#eeeeee 60%,#4c6789);"></div>
    <svg class="layer" width="212" height="212" viewBox="0 0 212 212" aria-hidden="true">
      <polygon fill="var(--white)" points="150,0 212,0 212,186 90,186"/>
      <polygon fill="var(--blue)" points="146,0 152,0 92,186 84,186"/>
    </svg>
    <div class="brand" style="left:150px; width:62px; top:14px;">
      <span class="brand-square" style="width:30px; height:34px;"></span>
      <span class="brand-name" style="font-size:15px;">VELTRA</span>
    </div>
    <div class="headline" style="left:128px; top:78px; font-size:19px;">
      <span class="line-blue">VELTRA</span><span class="line-black">CLOTHING</span>
    </div>
    <div class="tee" role="img" aria-label="White t-shirt mockup with brand print" style="left:130px; top:132px; width:34px; height:44px;">
      <div class="tee-print"><span class="brand-square" style="width:8px; height:8px;"></span><span class="brand-name" style="font-size:5px;">VELTRA</span></div>
    </div>
    <div class="tee" role="img" aria-label="White t-shirt mockup with brand print" style="left:168px; top:130px; width:38px; height:48px;">
      <div class="tee-print"><span class="brand-square" style="width:9px; height:9px;"></span><span class="brand-name" style="font-size:5px;">VELTRA</span></div>
    </div>
    <div class="ring" style="left:70px; top:104px; width:60px; height:60px;">
      <svg width="60" height="60" viewBox="0 0 60 60" aria-hidden="true">
        <circle cx="30" cy="30" r="26" fill="var(--ring-grey)"/>
        <circle cx="30" cy="30" r="28" fill="none" stroke="var(--white)" stroke-width="3" stroke-dasharray="132 44" transform="rotate(-90 30 30)"/>
      </svg>
      <div class="ring-label"><span style="font-size:9px;">VERY SOON</span><span style="font-size:11px;">75%</span></div>
    </div>
    <div class="contact-bar" style="height:26px; font-size:5px;">
      <span><span class="dot"></span>0100.222.3344</span>
      <span><span class="dot"></span>www.veltra.shop</span>
      <span><span class="dot"></span>www.veltra.style</span>
    </div>
  </article>
</section>

<section class="story-row">

  <!-- Story 1 -->
  <article class="story story-duo" style="background: var(--white);">
    <div class="photo" role="img" aria-label="Photo of a woman in a white tee outdoors among greenery" style="left:0; top:0; width:190px; height:458px; background: linear-gradient(180deg,#4e5d3c 0%,#8c8f6c 25%,#f1f1f1 45%,#ececec 75%,#3f5a80);"></div>
    <svg class="layer" width="280" height="498" viewBox="0 0 280 498" aria-hidden="true">
      <polygon fill="var(--white)" points="190,0 280,0 280,458 80,458"/>
      <polygon fill="var(--blue)" points="178,0 192,0 84,458 70,458"/>
    </svg>
    <div class="brand" style="left:190px; width:90px; top:38px;">
      <span class="brand-square" style="width:42px; height:48px;"></span>
      <span class="brand-name" style="font-size:22px;">VELTRA</span>
    </div>
    <div class="headline" style="left:170px; top:128px; font-size:26px;">
      <span class="line-blue">VELTRA</span><span class="line-black">CLOTHING</span>
    </div>
    <div class="tee" role="img" aria-label="Large white t-shirt mockup with brand print" style="left:100px; top:222px; width:180px; height:236px;">
      <div class="tee-print"><span class="brand-square" style="width:58px; height:52px;"></span><span class="brand-name" style="font-size:28px;">VELTRA</span></div>
    </div>
    <div class="tee" role="img" aria-label="Small white t-shirt mockup with brand print" style="left:52px; top:334px; width:96px; height:124px;">
      <div class="tee-print"><span class="brand-square" style="width:22px; height:22px;"></span><span class="brand-name" style="font-size:11px;">VELTRA</span></div>
    </div>
    <div class="contact-bar" style="height:40px; font-size:6.5px;">
      <span><span class="dot"></span>0100.222.3344</span>
      <span><span class="dot"></span>www.veltra.shop</span>
      <span><span class="dot"></span>www.veltra.style</span>
    </div>
  </article>

  <!-- Story 2 -->
  <article class="story story-grey" style="background: var(--grey);">
    <div class="photo" role="img" aria-label="Photo of a smiling young man wearing a white tee" style="left:140px; top:20px; width:140px; height:440px; background: linear-gradient(175deg,#7a5843 0%,#cfae97 22%,#f5f5f5 40%,#e4e4e4 80%,#3a4a66);"></div>
    <svg class="layer" width="280" height="498" viewBox="0 0 280 498" aria-hidden="true">
      <polygon fill="var(--black)" points="0,0 280,0 280,4 220,12 170,6 110,14 60,8 0,24"/>
      <polygon fill="var(--black)" points="0,458 60,448 120,456 190,444 240,452 280,440 280,498 0,498"/>
      <polygon fill="var(--white)" points="22,0 110,0 110,76 66,98 22,76"/>
    </svg>
    <div class="brand" style="left:22px; width:88px; top:20px;">
      <span class="brand-square" style="width:36px; height:36px;"></span>
      <span class="brand-name" style="font-size:18px;">VELTRA</span>
    </div>
    <div class="headline" style="left:20px; top:140px; font-size:33px;">
      <span class="line-black">VELTRA</span><span class="line-blue">CLOTHING</span>
    </div>
    <div class="tee" role="img" aria-label="White t-shirt mockup with brand print" style="left:14px; top:248px; width:148px; height:182px;">
      <div class="tee-print"><span class="brand-square" style="width:26px; height:26px;"></span><span class="brand-name" style="font-size:12px;">VELTRA</span></div>
    </div>
    <div class="handle" style="left:58px; top:470px; font-size:8px; color: var(--white);"><span class="dot"></span>@veltraclothing.com</div>
  </article>

  <!-- Story 3 -->
  <article class="story story-torn" style="background: var(--white);">
    <div class="photo" role="img" aria-label="Photo of a blonde woman in a white tee and jeans" style="left:160px; top:0; width:120px; height:498px; background: linear-gradient(180deg,#5b4a3f 0%,#c7a98f 25%,#f0f0f0 45%,#e3e3e3 68%,#56708f);"></div>
    <svg class="layer" width="280" height="498" viewBox="0 0 280 498" aria-hidden="true">
      <polygon fill="var(--black)" points="170,0 184,0 176,60 190,130 172,200 186,270 168,340 182,420 172,498 160,498 170,420 156,340 172,270 158,200 174,130 162,60"/>
    </svg>
    <div class="brand" style="left:40px; width:90px; top:26px;">
      <span class="brand-square" style="width:52px; height:58px;"></span>
      <span class="brand-name" style="font-size:26px;">VELTRA</span>
    </div>
    <div class="headline" style="left:18px; top:146px; font-size:33px;">
      <span class="line-blue">VELTRA</span><span class="line-black">CLOTHING</span>
    </div>
    <div class="tee" role="img" aria-label="White t-shirt mockup with brand print" style="left:20px; top:250px; width:136px; height:170px;">
      <div class="tee-print"><span class="brand-square" style="width:40px; height:40px;"></span><span class="brand-name" style="font-size:18px;">VELTRA</span></div>
    </div>
    <div class="contacts" style="left:20px; top:442px; font-size:7px;">
      <div><span class="dot"></span>0100.222.3344</div>
      <div><span class="dot"></span>www.veltra.shop</div>
      <div><span class="dot"></span>www.veltra.style</div>
    </div>
  </article>
</section>

</body>
</html>
```